Website Design

Looking for a less than 30 page website for a new tree service company. Most of the pages would be copies of one another but for each geographical area we service. So, for five areas, we would replicate six services for each area.

Coding

Coded - Design and coding required

```html
<!DOCTYPE html>
<html lang="en">
<head>
<meta charset="utf-8">
<title>Oakline Trees — Tree Services</title>
<link href="https://fonts.googleapis.com/css2?family=Poppins:wght@500;600;700;800&family=Figtree:wght@400;500;600;700&display=swap" rel="stylesheet">
<style>
:root{
  --green-dark:#1c3f14;
  --green:#21480f;
  --green-deep:#1d4a34;
  --gold:#e3a823;
  --gold-light:#f0b92e;
  --white:#ffffff;
  --text:#3c3c3c;
  --muted:#6b6b6b;
  --line:#dcdcdc;
}
*{margin:0;padding:0;box-sizing:border-box}
html,body{width:1200px;height:4489px;overflow:hidden}
body{position:relative;background:var(--white);font-family:"Figtree",sans-serif;color:var(--text)}
.abs{position:absolute}
.heading{font-family:"Poppins",sans-serif;font-weight:700}

/* top bar */
.topbar{left:0;top:0;width:1200px;height:50px;background:var(--green-dark);color:var(--white);font-size:13px;font-weight:600}
.topbar .addr{left:58px;top:17px;display:flex;gap:10px;align-items:center}
.topbar .mail{left:850px;top:17px;display:flex;gap:8px;align-items:center}
.topbar .socials{left:1034px;top:19px;display:flex;gap:14px}
.topbar .socials span{width:11px;height:11px;border-radius:50%;background:var(--gold)}

/* nav */
.nav{left:0;top:50px;width:1200px;height:84px;background:var(--white)}
.nav a{position:absolute;top:31px;font-size:20px;font-weight:500;color:#222;text-decoration:none}
.nav .cta{left:1002px;top:25px;width:153px;height:42px;border-radius:21px;background:var(--gold);color:var(--white);font-size:17px;display:flex;align-items:center;justify-content:center}
.brand{left:530px;top:54px;width:120px;height:120px;border-radius:50%;background:var(--white);border:4px solid var(--gold);display:flex;align-items:center;justify-content:center;text-align:center;font-family:"Poppins",sans-serif;font-weight:700;font-size:19px;line-height:1.1;color:var(--green-dark);z-index:3}

/* hero */
.hero{left:0;top:134px;width:1200px;height:720px}
.hero-text{left:0;top:134px;width:1200px;text-align:center;color:var(--white)}
.hero-text .eyebrow{margin-top:140px;font-size:11px;font-weight:700;color:var(--gold);letter-spacing:.3px}
.hero-text h1{font-family:"Poppins",sans-serif;font-weight:700;font-size:70px;line-height:83px;margin-top:8px}
.btn{display:inline-flex;align-items:center;justify-content:center;background:var(--gold);color:var(--white);border-radius:20px;font-size:16px;font-weight:500}
.hero-text .btn{margin-top:22px;width:190px;height:40px}

/* about */
.about-img{left:136px;top:955px;width:383px;height:440px}
.about-copy{left:610px;top:1025px;width:460px}
.about-copy h2{font-family:"Poppins",sans-serif;font-weight:700;font-size:50px;line-height:61px;color:var(--green)}
.about-copy p{font-size:12px;line-height:16px;color:#555;margin-top:14px;padding-left:4px}
.about-copy .btn{margin-top:26px;width:210px;height:42px;font-size:18px}

/* services */
.services-band{left:0;top:1481px;width:1200px;height:322px}
.services-title{left:0;top:1530px;width:1200px;text-align:center;color:var(--white);font-size:50px}
.card{width:198px;height:420px;top:1651px;background:var(--white);border-radius:99px;border:1.5px solid #e6e6e6;text-align:center}
.card .photo{position:absolute;left:12px;top:10px;width:174px;height:174px;border-radius:50%;border:5px solid var(--gold)}
.card h3{position:absolute;top:210px;left:0;width:100%;font-family:"Poppins",sans-serif;font-size:19px;font-weight:600;line-height:25px;color:#1a1a1a}
.card p{position:absolute;top:272px;left:14px;right:14px;font-size:11.5px;line-height:15px;color:#555}
.card .arrow{position:absolute;left:76px;top:371px;width:44px;height:44px;border-radius:50%;background:var(--green-dark);display:flex;align-items:center;justify-content:center}

/* gallery */
.gallery-title{left:0;top:2130px;width:1200px;text-align:center;font-size:40px;color:var(--green)}
.tile{border-radius:6px}

/* areas */
.areas{left:0;top:2683px;width:1200px;height:463px}
.areas-title{left:0;top:2715px;width:1200px;text-align:center;font-size:52px;color:var(--white)}
.area{width:200px;text-align:center;color:var(--white)}
.area .dot{width:76px;height:76px;border-radius:50%;margin:0 auto;background:linear-gradient(#dff1cf 0 35%,#5a9e3a 35% 60%,#cfe6c2 60%)}
.area span{display:block;margin-top:12px;font-family:"Poppins",sans-serif;font-weight:600;font-size:24px}

/* contact */
.contact-title{left:64px;top:3280px;font-size:48px;color:var(--green)}
.info{left:66px;width:370px;height:87px;border:1.5px solid #e0e0e0;border-radius:3px;background:var(--white)}
.info svg{position:absolute;left:20px;top:24px}
.info h4{position:absolute;left:72px;top:24px;font-size:15px;font-weight:700;color:#222}
.info p{position:absolute;left:72px;top:48px;font-size:11px;color:#555}
.form{left:589px;top:3257px;width:556px;height:575px;background:var(--white);box-shadow:0 0 24px rgba(0,0,0,.07)}
.form label{position:absolute;font-size:12px;font-weight:600;color:#333}
.form label b{color:#d33}
.field{position:absolute;border:1.5px solid #d7d7d7;font-size:12px;color:#777;padding:0 16px;display:flex;align-items:center}
.send{position:absolute;left:35px;top:490px;width:484px;height:50px;border-radius:4px;background:var(--green-deep);color:var(--white);font-weight:700;font-size:15px;display:flex;align-items:center;justify-content:center}

/* footer */
.footer-shape{left:0;top:3880px;width:1200px;height:609px}
.footer-brand{left:548px;top:3884px;width:124px;height:124px;border-radius:50%;background:var(--white);border:4px solid var(--gold);display:flex;align-items:center;justify-content:center;text-align:center;font-family:"Poppins",sans-serif;font-weight:700;font-size:19px;line-height:1.1;color:var(--green-dark)}
.fcol{top:4096px;color:var(--white)}
.fcol h5{font-size:16px;font-weight:700}
.fcol .dash{width:18px;height:2px;background:var(--gold);margin-top:20px}
.fcol p{font-size:13px;line-height:25px}
.fcol ul{list-style:none;font-size:13px}
.fcol li{height:37px;display:flex;gap:16px;align-items:flex-start}
.fcol li:before{content:"";width:4px;height:4px;border-radius:50%;background:#b9c7b0;margin-top:7px}
.post{font-size:13px;line-height:20px}
.post small{display:block;font-size:9px;line-height:16px;margin-top:2px}
.fsoc{top:4315px;width:30px;height:30px;border-radius:50%;border:1px solid rgba(255,255,255,.35)}
.copyright{left:0;top:4464px;width:1200px;text-align:center;color:#e9eee4;font-size:13px}
</style>
</head>
<body>

<header class="abs topbar">
  <div class="abs addr">
    <svg width="10" height="13" viewBox="0 0 10 13"><path d="M5 0a5 5 0 0 0-5 5c0 3.5 5 8 5 8s5-4.5 5-8a5 5 0 0 0-5-5zm0 7a2 2 0 1 1 0-4 2 2 0 0 1 0 4z" fill="var(--gold)"/></svg>
    418 Cedar Hollow Road, WA 98000
  </div>
  <div class="abs mail">
    <svg width="14" height="11" viewBox="0 0 14 11"><rect x="1" y="1" width="12" height="9" fill="none" stroke="var(--gold)" stroke-width="1.5"/><path d="M1 1l6 5 6-5" fill="none" stroke="var(--gold)" stroke-width="1.5"/></svg>
    hello@oaklinetrees.example
  </div>
  <div class="abs socials"><span></span><span></span><span></span><span></span></div>
</header>

<nav class="abs nav">
  <a style="left:60px">Home</a>
  <a style="left:168px">About</a>
  <a style="left:272px">Services</a>
  <a style="left:392px">Gallery</a>
  <a style="left:727px">Reviews</a>
  <a style="left:846px">Blog</a>
  <a class="cta">Contact Now</a>
</nav>
<div class="abs brand">Oakline<br>Trees</div>

<svg class="abs hero" viewBox="0 0 1200 720" role="img" aria-label="Photo of an arborist in ear protection operating a log saw in a forest">
  <defs>
    <linearGradient id="heroPhoto" x1="0" y1="0" x2="1" y2="0">
      <stop offset="0" stop-color="#4a4636"/>
      <stop offset=".45" stop-color="#5d5544"/>
      <stop offset=".8" stop-color="#6a4a2a"/>
      <stop offset="1" stop-color="#4e3b26"/>
    </linearGradient>
  </defs>
  <rect width="1200" height="720" fill="#fff"/>
  <path d="M0 0H1200V555C1000 640 800 700 600 690 380 680 180 610 0 530Z" fill="url(#heroPhoto)"/>
  <path d="M0 530C180 610 380 680 600 690 800 700 1000 640 1200 555V590C1000 690 800 718 600 716 360 712 160 680 0 610Z" fill="var(--gold)"/>
</svg>
<div class="abs hero-text">
  <div class="eyebrow">TREE SERVICES COMPANY</div>
  <h1>Providing<br>High Quality<br>Tree Services</h1>
  <span class="btn">GET A FREE QUOTE</span>
</div>

<svg class="abs about-img" viewBox="0 0 383 440" role="img" aria-label="Photo of a hollow cut log with a chainsaw, framed in a hexagon with a bee illustration">
  <defs>
    <linearGradient id="logPhoto" x1="0" y1="0" x2="1" y2="1">
      <stop offset="0" stop-color="#a89270"/>
      <stop offset=".5" stop-color="#8a6a44"/>
      <stop offset="1" stop-color="#5f7a3a"/>
    </linearGradient>
  </defs>
  <polygon points="191,8 375,114 375,326 191,432 8,326 8,114" fill="none" stroke="var(--gold)" stroke-width="4"/>
  <polygon points="191,22 362,121 362,319 191,418 21,319 21,121" fill="url(#logPhoto)"/>
</svg>
<div class="abs about-copy">
  <h2>The Best Choice For Tree Services</h2>
  <p>Lorem ipsum dolor sit amet, consectetur adipiscing elit, sed do eiusmod tempor incididunt ut labore et dolore magna aliqua. Ut enim ad minim veniam, quis nostrud exercitation ullamco.</p>
  <p>Lorem ipsum dolor sit amet, consectetur adipiscing elit, sed do eiusmod tempor incididunt ut labore et dolore magna aliqua. Ut enim ad minim veniam, quis nostrud exercitation ullamco.</p>
  <span class="btn">GET A FREE QUOTE</span>
</div>

<div class="abs services-band" role="img" aria-label="Dark green photo of a tree trunk and forest" style="background:linear-gradient(90deg,#2b4a1c,#3c5a26 50%,#2d4a1e)"></div>
<h2 class="abs heading services-title">Our Services</h2>

<div class="abs card" style="left:139px">
  <div class="photo" role="img" aria-label="Photo of a cut log and chainsaw" style="background:linear-gradient(135deg,#a48a66,#7a5a36)"></div>
  <h3>COMMERCIAL<br>SERVICES</h3>
  <p>Lorem ipsum dolor sit amet, consectetur adipiscing elit, sed do eiusmod tempor</p>
  <div class="arrow"><svg width="16" height="14" viewBox="0 0 16 14"><path d="M0 7H13M8 1l6 6-6 6" fill="none" stroke="#fff" stroke-width="2.5"/></svg></div>
</div>
<div class="abs card" style="left:380px">
  <div class="photo" role="img" aria-label="Photo of a worker clearing autumn leaves" style="background:linear-gradient(135deg,#4d5a2a,#8a4a1c)"></div>
  <h3>TREE<br>REMOVAL</h3>
  <p>Lorem ipsum dolor sit amet, consectetur adipiscing elit, sed do eiusmod tempor</p>
  <div class="arrow"><svg width="16" height="14" viewBox="0 0 16 14"><path d="M0 7H13M8 1l6 6-6 6" fill="none" stroke="#fff" stroke-width="2.5"/></svg></div>
</div>
<div class="abs card" style="left:620px">
  <div class="photo" role="img" aria-label="Photo of an arborist with a chainsaw in protective gear" style="background:linear-gradient(135deg,#3f6a2a,#7a5a3a)"></div>
  <h3 style="top:206px">PRUNING &amp;<br>TRIMMING</h3>
  <p style="top:268px">Lorem ipsum dolor sit amet, consectetur adipiscing elit, sed do eiusmod tempor</p>
  <div class="arrow"><svg width="16" height="14" viewBox="0 0 16 14"><path d="M0 7H13M8 1l6 6-6 6" fill="none" stroke="#fff" stroke-width="2.5"/></svg></div>
</div>
<div class="abs card" style="left:860px">
  <div class="photo" role="img" aria-label="Photo of gloved hands pruning a shrub" style="background:linear-gradient(135deg,#2f5a22,#4e7a34)"></div>
  <h3>TREE CARE<br>SERVIES</h3>
  <p style="top:266px">Lorem ipsum dolor sit amet, consectetur adipiscing elit, sed do eiusmod tempor</p>
  <div class="arrow"><svg width="16" height="14" viewBox="0 0 16 14"><path d="M0 7H13M8 1l6 6-6 6" fill="none" stroke="#fff" stroke-width="2.5"/></svg></div>
</div>

<h2 class="abs heading gallery-title">Our Gallery</h2>
<div class="abs tile" role="img" aria-label="Photo of trees beside a brick house" style="left:158px;top:2238px;width:281px;height:149px;background:linear-gradient(135deg,#5f8a3c,#3e5a2a 60%,#8a5a44)"></div>
<div class="abs tile" role="img" aria-label="Photo of a potted seedling in soil" style="left:162px;top:2427px;width:280px;height:150px;background:linear-gradient(180deg,#6a9a3a,#4a3a2a)"></div>
<div class="abs tile" role="img" aria-label="Photo of a worker with a leaf blower in an autumn park" style="left:486px;top:2226px;width:253px;height:352px;background:linear-gradient(180deg,#4e5a34,#6a4a24 60%,#8a4a1a)"></div>
<div class="abs tile" role="img" aria-label="Photo of a cut log with a chainsaw" style="left:777px;top:2233px;width:280px;height:148px;background:linear-gradient(135deg,#a8906c,#7a5a3a 60%,#6a7a3a)"></div>
<div class="abs tile" role="img" aria-label="Photo of a family playing by a garden shed" style="left:781px;top:2421px;width:280px;height:150px;background:linear-gradient(135deg,#5a7a3a,#7a4a2a 50%,#6a8a4a)"></div>

<div class="abs areas" role="img" aria-label="Dark green photo of a garden shed and trees" style="background:linear-gradient(90deg,#2e4822,#3b5a2a 50%,#2c4620)"></div>
<h2 class="abs heading areas-title">Areas We Served</h2>
<div class="abs area" style="left:67px;top:2819px"><div class="dot"></div><span>Location 1</span></div>
<div class="abs area" style="left:283px;top:2819px"><div class="dot"></div><span>Location 2</span></div>
<div class="abs area" style="left:499px;top:2819px"><div class="dot"></div><span>Location 3</span></div>
<div class="abs area" style="left:715px;top:2819px"><div class="dot"></div><span>Location 4</span></div>
<div class="abs area" style="left:931px;top:2819px"><div class="dot"></div><span>Location 5</span></div>
<div class="abs area" style="left:72px;top:2967px"><div class="dot"></div><span>Location 6</span></div>
<div class="abs area" style="left:288px;top:2967px"><div class="dot"></div><span>Location 7</span></div>
<div class="abs area" style="left:504px;top:2967px"><div class="dot"></div><span>Location 8</span></div>
<div class="abs area" style="left:720px;top:2967px"><div class="dot"></div><span>Location 9</span></div>
<div class="abs area" style="left:936px;top:2967px"><div class="dot"></div><span>Location 10</span></div>

<h2 class="abs heading contact-title">Contact Us</h2>
<div class="abs info" style="top:3423px">
  <svg width="26" height="34" viewBox="0 0 26 34"><path d="M13 0a13 13 0 0 0-13 13c0 9 13 21 13 21s13-12 13-21A13 13 0 0 0 13 0zm0 18a5 5 0 1 1 0-10 5 5 0 0 1 0 10z" fill="var(--gold)"/></svg>
  <h4>Our Address</h4><p>14 Birch Lane, Maple Ridge</p>
</div>
<div class="abs info" style="top:3533px">
  <svg width="30" height="30" viewBox="0 0 30 30"><path d="M7 2l5 7-3 3c2 4 5 7 9 9l3-3 7 5-3 5C13 27 3 17 2 5z" fill="var(--gold)"/></svg>
  <h4>Our Phone</h4><p>000 5550 18273</p>
</div>
<div class="abs info" style="top:3643px">
  <svg width="32" height="30" viewBox="0 0 32 30"><rect x="2" y="10" width="28" height="18" fill="none" stroke="var(--gold)" stroke-width="2"/><path d="M2 10l14 10 14-10M8 10V3h16v7" fill="none" stroke="var(--gold)" stroke-width="2"/></svg>
  <h4>Our Email</h4><p>office@oaklinetrees.example</p>
</div>

<div class="abs form">
  <label style="left:35px;top:62px">Name (required) <b>*</b></label>
  <div class="field" style="left:35px;top:96px;width:229px;height:58px">Full Name</div>
  <label style="left:289px;top:62px">Phone (optional) <b>*</b></label>
  <div class="field" style="left:289px;top:96px;width:230px;height:58px">Phone Number</div>
  <label style="left:35px;top:182px">Email address (required) <b>*</b></label>
  <div class="field" style="left:35px;top:213px;width:229px;height:58px">Email Address</div>
  <label style="left:289px;top:182px">Services (required) <b>*</b></label>
  <div class="field" style="left:289px;top:213px;width:230px;height:58px;justify-content:space-between">Choose services <span>&#215;</span></div>
  <label style="left:35px;top:300px">Your message*</label>
  <div class="field" style="left:35px;top:335px;width:484px;height:124px;align-items:flex-start;padding-top:16px">Your Message</div>
  <div class="send">Send message</div>
</div>

<svg class="abs footer-shape" viewBox="0 0 1200 609">
  <path d="M0 175C200 90 400 55 600 55S1000 95 1200 150V609H0Z" fill="var(--gold)"/>
  <path d="M0 200C200 130 400 100 600 100S1000 130 1200 185V609H0Z" fill="var(--green-deep)"/>
  <circle cx="1106" cy="606" r="22" fill="none" stroke="#fff" stroke-width="1.5"/>
  <path d="M1100 605l6-6 6 6" fill="none" stroke="#fff" stroke-width="2"/>
</svg>
<div class="abs footer-brand">Oakline<br>Trees</div>

<div class="abs fcol" style="left:115px;width:220px">
  <h5>About Us</h5><div class="dash"></div>
  <p style="margin-top:34px">Lorem Ipsum simply dummy text available in market the printing text. MORE...</p>
</div>
<div class="abs fsoc" style="left:117px"></div>
<div class="abs fsoc" style="left:164px"></div>
<div class="abs fsoc" style="left:211px"></div>
<div class="abs fsoc" style="left:258px"></div>

<div class="abs fcol" style="left:392px;width:170px">
  <h5>Explore</h5><div class="dash"></div>
  <ul style="margin-top:38px"><li>Emergency Services</li><li>Tree Removal</li><li>Tree Cutting</li><li>Plantation</li></ul>
</div>
<div class="abs fcol" style="left:578px;width:210px">
  <h5>Recent Post</h5><div class="dash"></div>
  <div class="post" style="margin-top:30px;padding-left:12px">Everything You Need To Know About Lawn Maintenance Drought<small>01 Feb 2024</small></div>
  <div class="post" style="margin-top:12px;padding-left:12px">Benefits Of Tree Coverage: Is Your Home Made In The Shade?<small>01 Feb 2024</small></div>
</div>
<div class="abs fcol" style="left:815px;width:300px">
  <h5>Newsletter</h5><div class="dash"></div>
  <div style="margin-top:36px;height:31px;background:#fff;color:#999;font-size:10px;padding:10px 14px">Email</div>
  <div style="margin-top:11px;height:41px;background:var(--gold);border-radius:4px;display:flex;align-items:center;justify-content:center;font-size:13px;font-weight:700">Subscribe Now</div>
</div>
<div class="abs copyright">copyright 2024 Oakline Tree Services. All Rights Reserved.</div>

</body>
</html>
```